Designing Forms for Steady Ledger

I need to create professional forms that can be edited in Microsoft Word. 1. I would like the forms to include our logo (see upload). I have this logo as a PDF, JPG, or source file (.ZIP). I would like the logo to be blue.2. I would like the forms to be readable from top to bottom of the page when viewing in portrait layout, not landscape layout. 3. I have included samples of the forms I have created. Some of them are in landscape mode and need to be changed. The text in the information cells are just examples so you can see what will be used as inputs, but the forms should not have data on them except for the titles and column headers. 4. There are 6 different forms.

Target Market(s)

Individuals and families

Industry/Entity Type

Financial Planning

Requirements
Must have
• Logo
• Portrait layout

```html
<!DOCTYPE html>
<html lang="en">
<head>
<meta charset="utf-8">
<title>Keycodes and Passwords</title>
<link href="https://fonts.googleapis.com/css2?family=Carlito:wght@400;700&display=swap" rel="stylesheet">
<style>
  :root {
    --backdrop: #1c1c1c;
    --paper: #ffffff;
    --navy: #1f3864;
    --brand-blue: #1f5fa8;
    --header-blue: #3f6cb0;
    --header-text: #ffffff;
  }
  * { box-sizing: border-box; margin: 0; padding: 0; }
  html, body {
    width: 1200px;
    height: 1000px;
    overflow: hidden;
    background: var(--backdrop);
    font-family: "Carlito", "Calibri", Arial, sans-serif;
  }
  .page {
    position: absolute;
    left: 258px;
    top: 18px;
    width: 734px;
    height: 950px;
    background: var(--paper);
  }
  .brand {
    position: absolute;
    right: 70px;
    top: 47px;
    display: flex;
    align-items: center;
    gap: 14px;
  }
  .brand-name {
    font-weight: 700;
    font-size: 30px;
    letter-spacing: 1px;
    color: var(--brand-blue);
    line-height: 1;
  }
  .brand-mark { display: block; }
  .form-title {
    position: absolute;
    left: 52px;
    top: 122px;
    font-size: 27px;
    font-weight: 700;
    color: var(--navy);
    line-height: 1;
  }
  .entry-table {
    position: absolute;
    left: 45px;
    top: 157px;
    width: 623px;
    border-collapse: collapse;
    table-layout: fixed;
  }
  .entry-table th,
  .entry-table td {
    border: 2px solid var(--navy);
  }
  .entry-table th {
    height: 37px;
    background: var(--header-blue);
    color: var(--header-text);
    font-size: 15px;
    font-weight: 700;
    text-align: center;
  }
  .entry-table td { height: 33.75px; }
  .col-title, .col-location, .col-password { width: 133px; }
  .col-notes { width: 224px; }
</style>
</head>
<body>
  <main class="page">
    <header class="brand">
      <span class="brand-name">STEADY LEDGER</span>
      <svg class="brand-mark" width="72" height="72" viewBox="0 0 72 72" aria-hidden="true">
        <circle cx="36" cy="36" r="33" fill="none" stroke="var(--brand-blue)" stroke-width="3"/>
      </svg>
    </header>

    <h1 class="form-title">KEYCODES and PASSWORDS</h1>

    <table class="entry-table">
      <colgroup>
        <col class="col-title"><col class="col-location"><col class="col-password"><col class="col-notes">
      </colgroup>
      <thead>
        <tr><th>Title</th><th>Location</th><th>Password</th><th></th></tr>
      </thead>
      <tbody>
        <tr><td></td><td></td><td></td><td></td></tr>
        <tr><td></td><td></td><td></td><td></td></tr>
        <tr><td></td><td></td><td></td><td></td></tr>
        <tr><td></td><td></td><td></td><td></td></tr>
        <tr><td></td><td></td><td></td><td></td></tr>
        <tr><td></td><td></td><td></td><td></td></tr>
        <tr><td></td><td></td><td></td><td></td></tr>
        <tr><td></td><td></td><td></td><td></td></tr>
        <tr><td></td><td></td><td></td><td></td></tr>
        <tr><td></td><td></td><td></td><td></td></tr>
        <tr><td></td><td></td><td></td><td></td></tr>
        <tr><td></td><td></td><td></td><td></td></tr>
        <tr><td></td><td></td><td></td><td></td></tr>
        <tr><td></td><td></td><td></td><td></td></tr>
        <tr><td></td><td></td><td></td><td></td></tr>
        <tr><td></td><td></td><td></td><td></td></tr>
        <tr><td></td><td></td><td></td><td></td></tr>
        <tr><td></td><td></td><td></td><td></td></tr>
        <tr><td></td><td></td><td></td><td></td></tr>
        <tr><td></td><td></td><td></td><td></td></tr>
      </tbody>
    </table>
  </main>
</body>
</html>
```